Flyer
Zielgruppe
Ich möchte den bisher erstellten Flyer (habe ich hochgeladen) ein wnig 'umstylen', mit dem neuen Logo. Der 200 Euro Bonus sol als Geldschein dargestellt werden.

```html
<!DOCTYPE html>
<html lang="de">
<head>
<meta charset="utf-8">
<title>Juris Salon – Flyer</title>
<link href="https://fonts.googleapis.com/css2?family=Playfair+Display:wght@400;500&family=Poppins:wght@400;500&display=swap" rel="stylesheet">
<style>
  :root {
    --page: #e9e9e7;
    --ink: #141312;
    --gold: #e9c98a;
    --gold-light: #f6e2b0;
    --gold-deep: #c89a4e;
    --gold-dark: #6e5128;
    --ember: #ff9a2e;
    --text: #efe3c8;
    --note-a: #2a2114;
    --note-b: #4a3820;
  }
  * { margin: 0; padding: 0; box-sizing: border-box; }
  html, body { width: 1200px; height: 848px; overflow: hidden; background: var(--page); }
  .canvas { position: relative; width: 1200px; height: 848px; }

  .flyer {
    position: absolute; top: 130px; width: 416px; height: 588px; overflow: hidden;
    background:
      radial-gradient(ellipse 60% 40% at 100% 10%, rgba(201,154,78,.18), transparent 70%),
      radial-gradient(ellipse 55% 30% at 0% 100%, rgba(201,154,78,.16), transparent 70%),
      var(--ink);
    box-shadow: 0 6px 14px rgba(0,0,0,.18);
    color: var(--text);
  }
  .flyer--front { left: 162px; }
  .flyer--back { left: 622px;
    background:
      radial-gradient(ellipse 50% 30% at 100% 95%, rgba(201,154,78,.18), transparent 70%),
      radial-gradient(ellipse 40% 30% at 0% 50%, rgba(201,154,78,.12), transparent 70%),
      var(--ink);
  }

  .row { position: absolute; left: 0; right: 0; text-align: center; line-height: 1.2; white-space: nowrap; }
  .serif { font-family: "Playfair Display", Georgia, serif; }
  .sans { font-family: "Poppins", Arial, sans-serif; }

  .glow-line {
    position: absolute; left: 50%; height: 2px; transform: translateX(-50%);
    background: linear-gradient(90deg, transparent, rgba(200,110,40,.6) 20%, var(--ember) 45%, #fff3d0 50%, var(--ember) 55%, rgba(200,110,40,.6) 80%, transparent);
    box-shadow: 0 0 6px rgba(255,160,60,.6);
  }

  .brand-dot { position: absolute; left: 50%; top: 30px; width: 22px; height: 22px; margin-left: -11px; border-radius: 50%; background: var(--gold); }
  .brand-name { top: 66px; font-size: 29px; font-weight: 400; color: var(--gold); letter-spacing: 1px; }
  .brand-tagline { top: 101px; font-size: 12px; color: var(--gold); letter-spacing: .5px; }

  /* Bonus banknote */
  .banknote {
    position: absolute; left: 88px; top: 158px; width: 240px; height: 134px;
    border-radius: 4px;
    background:
      radial-gradient(ellipse 55% 70% at 50% 50%, rgba(246,226,176,.16), transparent 70%),
      linear-gradient(135deg, var(--note-b) 0%, var(--note-a) 45%, var(--note-b) 100%);
    border: 2px solid var(--gold-light);
    box-shadow: 0 0 18px 5px rgba(255,190,90,.45);
  }
  .banknote__inner {
    position: absolute; inset: 5px; border: 1px solid var(--gold-deep); border-radius: 2px;
  }
  .banknote__band {
    position: absolute; top: 0; bottom: 0; width: 6px; background: linear-gradient(180deg, var(--gold-deep), var(--gold-light), var(--gold-deep));
    opacity: .55;
  }
  .banknote__band--left { left: 48px; }
  .banknote__band--right { right: 48px; }
  .banknote__seal {
    position: absolute; top: 52px; width: 24px; height: 24px; border-radius: 50%;
    border: 1px solid var(--gold); 
  }
  .banknote__seal--left { left: 14px; }
  .banknote__seal--right { right: 14px; }
  .banknote__corner { position: absolute; font-family: "Poppins", Arial, sans-serif; font-size: 9px; font-weight: 500; color: var(--gold); line-height: 1; }
  .banknote__corner--tl { left: 11px; top: 10px; }
  .banknote__corner--tr { right: 11px; top: 10px; }
  .banknote__corner--bl { left: 11px; bottom: 10px; }
  .banknote__corner--br { right: 11px; bottom: 10px; }
  .banknote__label { top: 14px; font-size: 8.5px; color: var(--text); }
  .banknote__amount { top: 26px; font-family: "Poppins", Arial, sans-serif; font-size: 46px; font-weight: 500; color: var(--gold-light); letter-spacing: 1px; }
  .banknote__rule { position: absolute; left: 87px; width: 62px; top: 91px; height: 1px; background: var(--gold); }
  .banknote__word { top: 97px; font-size: 14px; color: var(--gold); letter-spacing: 1px; }

  .headline { font-size: 20px; color: var(--text); }
  .checklist { position: absolute; list-style: none; }
  .checklist li { position: absolute; left: 0; display: flex; align-items: center; white-space: nowrap; color: var(--text); }
  .checklist svg { flex: none; }

  .product-photo {
    position: absolute; left: 0; top: 0; width: 416px; height: 210px;
    background:
      linear-gradient(180deg, transparent 45%, var(--ink) 100%),
      linear-gradient(90deg, #bdb4a8 0%, #8a7665 35%, #5e4a3a 60%, #2a211b 100%);
  }
  .intro { top: 272px; font-size: 8px; line-height: 14.5px; white-space: normal; padding: 0 50px; }
</style>
</head>
<body>
<main class="canvas">

  <section class="flyer flyer--front">
    <span class="brand-dot"></span>
    <div class="row sans brand-name">Juris Salon</div>
    <div class="row sans brand-tagline">LAWYER NETWORK</div>
    <div class="glow-line" style="top:130px;width:300px"></div>

    <div class="banknote">
      <div class="banknote__inner"></div>
      <span class="banknote__band banknote__band--left"></span>
      <span class="banknote__band banknote__band--right"></span>
      <span class="banknote__seal banknote__seal--left"></span>
      <span class="banknote__seal banknote__seal--right"></span>
      <span class="banknote__corner banknote__corner--tl">200</span>
      <span class="banknote__corner banknote__corner--tr">200</span>
      <span class="banknote__corner banknote__corner--bl">200</span>
      <span class="banknote__corner banknote__corner--br">200</span>
      <div class="row serif banknote__label">Exklusiver Startvorteil für neue Mitglieder</div>
      <div class="row banknote__amount">€200</div>
      <div class="banknote__rule"></div>
      <div class="row serif banknote__word">BONUS</div>
    </div>

    <div class="row serif headline" style="top:322px">Das exklusive Netzwerk</div>
    <div class="row serif headline" style="top:344px">für ambitionierte Anwälte</div>
    <div class="glow-line" style="top:380px;width:290px"></div>

    <ul class="checklist sans" style="left:85px;top:0;font-size:10.5px">
      <li style="top:392px"><svg width="16" height="16" viewBox="0 0 16 16"><circle cx="8" cy="8" r="7" fill="none" stroke="var(--gold)" stroke-width="1.3"/><path d="M4.6 8.2l2.3 2.2 4.5-4.6" fill="none" stroke="var(--gold)" stroke-width="1.5"/></svg><span style="margin-left:9px">Hochwertiges Networking mit Top-Anwälten</span></li>
      <li style="top:418px"><svg width="16" height="16" viewBox="0 0 16 16"><circle cx="8" cy="8" r="7" fill="none" stroke="var(--gold)" stroke-width="1.3"/><path d="M4.6 8.2l2.3 2.2 4.5-4.6" fill="none" stroke="var(--gold)" stroke-width="1.5"/></svg><span style="margin-left:9px">Zugang zu exklusiven Events</span></li>
      <li style="top:443px"><svg width="16" height="16" viewBox="0 0 16 16"><circle cx="8" cy="8" r="7" fill="none" stroke="var(--gold)" stroke-width="1.3"/><path d="M4.6 8.2l2.3 2.2 4.5-4.6" fill="none" stroke="var(--gold)" stroke-width="1.5"/></svg><span style="margin-left:9px">Mehr Mandanten und neue Chancen</span></li>
    </ul>
    <div class="glow-line" style="top:476px;width:300px"></div>

    <div class="row serif" style="top:492px;font-size:13px">Jetzt Mitglied werden und <span class="sans" style="font-weight:500">€200</span> Bonus sichern</div>
    <div class="row serif" style="top:516px;font-size:8px">www.juris-salon.de</div>
    <div class="glow-line" style="top:537px;width:210px"></div>
    <div class="row serif" style="top:553px;font-size:10.5px">Exklusiv&nbsp; • &nbsp;Diskret&nbsp; • &nbsp;Erfolgreich.</div>
  </section>

  <section class="flyer flyer--back">
    <div class="product-photo" role="img" aria-label="Foto: Handschlag zweier Anwälte in einer Kanzlei"></div>

    <div class="row serif headline" style="top:188px">Ihr exklusives Netzwerk</div>
    <div class="row serif headline" style="top:214px">für Anwälte</div>
    <div class="glow-line" style="top:253px;width:245px"></div>

    <p class="row sans intro">Juris Salon verbindet ambitionierte Anwälte in einem hochwertigen und diskreten Netzwerk. Ziel ist es, neue Kontakte zu schaffen, Synergien zu nutzen und langfristigen Erfolg zu fördern.</p>
    <div class="glow-line" style="top:335px;width:235px"></div>

    <ul class="checklist sans" style="left:106px;top:0;font-size:8px">
      <li style="top:355px"><svg width="13" height="13" viewBox="0 0 16 16"><circle cx="8" cy="8" r="7" fill="none" stroke="var(--gold)" stroke-width="1.4"/><path d="M4.6 8.2l2.3 2.2 4.5-4.6" fill="none" stroke="var(--gold)" stroke-width="1.6"/></svg><span style="margin-left:6px">Aufbau eines starken beruflichen Netzwerks</span></li>
      <li style="top:375px"><svg width="13" height="13" viewBox="0 0 16 16"><circle cx="8" cy="8" r="7" fill="none" stroke="var(--gold)" stroke-width="1.4"/><path d="M4.6 8.2l2.3 2.2 4.5-4.6" fill="none" stroke="var(--gold)" stroke-width="1.6"/></svg><span style="margin-left:6px">Zugang zu ausgewählten Veranstaltungen</span></li>
      <li style="top:395px"><svg width="13" height="13" viewBox="0 0 16 16"><circle cx="8" cy="8" r="7" fill="none" stroke="var(--gold)" stroke-width="1.4"/><path d="M4.6 8.2l2.3 2.2 4.5-4.6" fill="none" stroke="var(--gold)" stroke-width="1.6"/></svg><span style="margin-left:6px">Austausch auf höchstem fachlichen Niveau</span></li>
      <li style="top:415px"><svg width="13" height="13" viewBox="0 0 16 16"><circle cx="8" cy="8" r="7" fill="none" stroke="var(--gold)" stroke-width="1.4"/><path d="M4.6 8.2l2.3 2.2 4.5-4.6" fill="none" stroke="var(--gold)" stroke-width="1.6"/></svg><span style="margin-left:6px">Neue Mandanten und Geschäftsmöglichkeiten</span></li>
    </ul>
    <div class="glow-line" style="top:444px;width:240px"></div>

    <div class="row serif" style="top:459px;font-size:19px">Jetzt <span class="sans" style="font-weight:500">€200</span> Bonus sichern:</div>
    <div class="row serif" style="top:500px;font-size:13px">www.juris-salon.de</div>
    <div class="glow-line" style="top:536px;width:165px"></div>
  </section>

</main>
</body>
</html>
```